Business card design for Bront Engineering Qavo

We need a new business card design along with all the necessary to place an order. The company is Bront Engineering Qavo and we recently updated our logo.

```html
<!DOCTYPE html>
<html lang="en">
<head>
<meta charset="utf-8">
<title>Bront Engineering Qavo – Business Card</title>
<link rel="stylesheet" href="https://fonts.googleapis.com/css2?family=Roboto:wght@300;400;500;700&display=swap">
<style>
  :root {
    --backdrop: #3a3a3a;
    --card-white: #fdfdfd;
    --brand-yellow: #e2be22;
    --brand-grey: #8e8e8e;
    --ink: #111111;
    --rule: rgba(17, 17, 17, 0.55);
  }
  * { box-sizing: border-box; margin: 0; padding: 0; }
  html, body {
    width: 1200px;
    height: 694px;
    overflow: hidden;
    background: var(--backdrop);
    font-family: "Roboto", Arial, sans-serif;
  }
  .canvas {
    position: relative;
    width: 1200px;
    height: 694px;
  }
  .card {
    position: absolute;
    top: 185px;
    width: 500px;
    height: 324px;
    border-radius: 30px;
    overflow: hidden;
  }
  .card--front {
    left: 60px;
    background: var(--card-white);
    display: flex;
    align-items: center;
    justify-content: center;
    gap: 14px;
  }
  .brand-mark {
    width: 22px;
    height: 22px;
    background: var(--brand-yellow);
  }
  .brand-name {
    color: var(--brand-grey);
    font-weight: 500;
    font-size: 27px;
    letter-spacing: 2px;
    text-transform: uppercase;
  }
  .card--back {
    left: 640px;
    background: var(--brand-yellow);
    color: var(--ink);
  }
  .holder {
    position: absolute;
    left: 40px;
    top: 44px;
    width: 200px;
    text-align: center;
  }
  .holder__name { font-size: 24px; font-weight: 500; }
  .holder__role {
    margin-top: 4px;
    font-size: 9px;
    letter-spacing: 4px;
    font-weight: 500;
  }
  .divider-vertical {
    position: absolute;
    left: 258px;
    top: 36px;
    width: 1px;
    height: 80px;
    background: var(--rule);
  }
  .rule {
    position: absolute;
    left: 36px;
    right: 36px;
    height: 1px;
    background: var(--rule);
  }
  .rule--upper { top: 134px; }
  .rule--lower { top: 294px; }
  .contact {
    position: absolute;
    font-size: 14px;
  }
  .contact__label {
    display: flex;
    align-items: center;
    gap: 6px;
    font-size: 9px;
    letter-spacing: 4px;
    font-weight: 500;
    margin-bottom: 4px;
  }
  .contact__label svg { width: 13px; height: 13px; }
  .contact--web { left: 282px; top: 52px; }
  .contact--email { left: 40px; top: 150px; font-size: 16px; }
  .contact--phone { left: 40px; top: 200px; }
  .phone-number {
    font-size: 60px;
    font-weight: 500;
    letter-spacing: 1px;
    line-height: 1;
  }
</style>
</head>
<body>
<main class="canvas">
  <section class="card card--front" aria-label="Card front">
    <span class="brand-mark" aria-hidden="true"></span>
    <span class="brand-name">Bront Engineering Qavo</span>
  </section>

  <section class="card card--back" aria-label="Card back">
    <div class="holder">
      <p class="holder__name">Helen Marlow</p>
      <p class="holder__role">DIRECTOR</p>
    </div>
    <div class="divider-vertical"></div>

    <div class="contact contact--web">
      <p class="contact__label">
        <svg viewBox="0 0 16 16" aria-hidden="true"><circle cx="8" cy="8" r="7" fill="none" stroke="currentColor" stroke-width="1.6"/><ellipse cx="8" cy="8" rx="3" ry="7" fill="none" stroke="currentColor" stroke-width="1.2"/><line x1="1" y1="8" x2="15" y2="8" stroke="currentColor" stroke-width="1.2"/></svg>
        WEB
      </p>
      <p>www.brontengineering.co.uk</p>
    </div>

    <div class="rule rule--upper"></div>

    <div class="contact contact--email">
      <p class="contact__label">
        <svg viewBox="0 0 16 16" aria-hidden="true"><rect x="1" y="3" width="14" height="10" fill="currentColor"/><polyline points="1,3 8,9 15,3" fill="none" stroke="#e2be22" stroke-width="1.4"/></svg>
        E-MAIL
      </p>
      <p>sales@brontengineering.co.uk</p>
    </div>

    <div class="contact contact--phone">
      <p class="contact__label">
        <svg viewBox="0 0 16 16" aria-hidden="true"><path d="M2 5c0-2 2-3 6-3s6 1 6 3l-3 1-1-2H6L5 6 2 5zM4 8h8l2 6H2l2-6z" fill="currentColor"/></svg>
        PHONE
      </p>
      <p class="phone-number">01632 960418</p>
    </div>

    <div class="rule rule--lower"></div>
  </section>
</main>
</body>
</html>
```